Lumora business card for a plastic surgeon

we need a business card for plastic surgeons that work on a clinic called LUMORA.
we want a clean design and the following informations: name of the doctor, doctor's registration number (called CRM), telephone, address, facebook, instagram.
Colors: white, blue tones, light brown/ coffee

facebook and instagram: lumoracirurgiaestetica

Industry/Entity Type

Business

Contact Information for Business Card

clean design

Font styles to use
Serif
Sans Serif
Other font styles liked:
• helvetica light

Colors
cee9f5
85cae6
85abd2
3276b5
cfeae6
cedeed
eaf1f7

Requirements
Must have
• doctor's name
• identification number (called CRM)
• contact (phone, facebook, instagram, address)

```html
<!DOCTYPE html>
<html lang="pt">
<head>
<meta charset="utf-8">
<title>Lumora – Business Card</title>
<link rel="stylesheet" href="https://fonts.googleapis.com/css2?family=Marcellus&family=Open+Sans:wght@400;600&display=swap">
<style>
  :root {
    --navy: #0b3562;
    --cyan: #12b9d9;
    --teal-deep: #0a5d93;
    --teal-light: #0f8fc4;
    --white: #ffffff;
    --stage: #eef1f4;
    --logo-font: "Marcellus", serif;
    --text-font: "Open Sans", sans-serif;
  }
  * { margin: 0; padding: 0; box-sizing: border-box; }
  html, body { width: 1200px; height: 900px; overflow: hidden; }
  body { background: var(--stage); position: relative; font-family: var(--text-font); }

  .card {
    position: absolute;
    overflow: hidden;
    box-shadow: 0 6px 18px rgba(0, 0, 0, 0.18);
  }

  /* Front */
  .card-front { left: 78px; top: 34px; width: 588px; height: 364px; background: var(--white); }
  .front-bands { position: absolute; inset: 0; }
  .brand { position: absolute; left: 0; width: 588px; text-align: center; }
  .brand-name {
    top: 42px;
    font-family: var(--logo-font);
    font-size: 64px;
    letter-spacing: 2px;
    color: var(--cyan);
    line-height: 1;
  }
  .brand-tagline {
    top: 124px;
    font-family: var(--logo-font);
    font-size: 25px;
    letter-spacing: 2px;
    color: var(--navy);
  }
  .contact-list {
    position: absolute; right: 326px; top: 232px;
    list-style: none; color: var(--white); font-size: 15px;
  }
  .contact-list li {
    display: flex; justify-content: flex-end; align-items: center;
    gap: 6px; height: 25px;
  }
  .contact-list svg { width: 12px; height: 12px; flex: none; }
  .doctor { position: absolute; left: 315px; top: 222px; color: var(--white); }
  .doctor-name { font-size: 20px; font-weight: 600; }
  .doctor-crm { font-size: 15px; margin-top: 2px; }
  .doctor-address { font-size: 15px; margin-top: 14px; line-height: 24px; }

  /* Back */
  .card-back {
    left: 388px; top: 506px; width: 566px; height: 350px;
    background: radial-gradient(ellipse at 50% 35%, var(--teal-light) 0%, var(--teal-deep) 55%, var(--navy) 100%);
  }
  .card-back .brand { width: 566px; }
  .card-back .brand-name { top: 196px; color: var(--white); font-size: 60px; }
  .card-back .brand-tagline { top: 274px; color: var(--white); font-size: 23px; }
</style>
</head>
<body>
  <section class="card card-front" aria-label="Business card front">
    <svg class="front-bands" width="588" height="364" viewBox="0 0 588 364" aria-hidden="true">
      <polygon points="0,182 404,182 382,210 0,210" fill="var(--cyan)"/>
      <polygon points="414,176 588,176 588,364 0,364 0,214 386,214" fill="var(--navy)"/>
    </svg>

    <div class="brand brand-name">LUMORA</div>
    <div class="brand brand-tagline">CIRURGIA PLÁSTICA</div>

    <ul class="contact-list">
      <li>(044)-456-7890
        <svg viewBox="0 0 12 12"><path d="M3 1l2 2.5-1.2 1.2a7 7 0 0 0 3.5 3.5L8.5 7 11 9l-1.3 2C5 11 1 7 1 2.3z" fill="currentColor"/></svg>
      </li>
      <li>info@youremail.com
        <svg viewBox="0 0 12 12"><rect x="0.5" y="2.5" width="11" height="7" fill="currentColor"/><path d="M0.5 2.5L6 7l5.5-4.5" stroke="var(--navy)" fill="none"/></svg>
      </li>
      <li>lumoracirurgiaestetica
        <svg viewBox="0 0 12 12"><circle cx="6" cy="6" r="5.5" fill="currentColor"/></svg>
      </li>
      <li>lumoracirurgiaestetica
        <svg viewBox="0 0 12 12"><rect x="0.5" y="0.5" width="11" height="11" rx="2" fill="currentColor"/></svg>
      </li>
    </ul>

    <div class="doctor">
      <div class="doctor-name">Doctor Name</div>
      <div class="doctor-crm">AB1241ABD</div>
      <div class="doctor-address">12345, Address Goes Here<br>Country Name, 123456</div>
    </div>
  </section>

  <section class="card card-back" aria-label="Business card back">
    <div class="brand brand-name">LUMORA</div>
    <div class="brand brand-tagline">CIRURGIA PLÁSTICA</div>
  </section>
</body>
</html>
```